Heal the world with your creativity.

We're looking for advertising materials (social media, email, etc) for a new mental health platform called PIM (www.seepim.example). PIM’s mission is to empower our members to heal and thrive by making expert advice and real-life experiences accessible to all.

Note

Facebook Cover Images: 820 x 312 pixels
LinkedIn Cover Images: 1128 x 191 pixels
3 x Social Media Post Image Templates: 1080 x 1080 pixles
3 x Enewsletter Header Image Templates: 1080 x 360 pixels
Sales One sheet: US Letter (8.5 x 11 inches)
Overview Powerpoint template: 13.33 x 7.5 inches

Fonts to Use:
Galanogrotesque
Montserrat regular

Target Market(s)

18 - 35 year olds

Industry/Entity Type

Mental Health

Requirements
Must have
• Facebook Cover Images: 820 x 312 pixels
3 x Enewsletter Header Images: 1080 x 360 pixels

Fonts to Use:
Galanogrotesque
Montserrat regular
Nice to have
• Creative copywriting for social media posts

```html
<!DOCTYPE html>
<html lang="en">
<head>
<meta charset="utf-8">
<title>PIM – In the middle of a storm</title>
<link rel="stylesheet" href="https://fonts.googleapis.com/css2?family=Montserrat:wght@600;700;800&display=swap">
<style>
  :root {
    --orange: #f7931e;
    --orange-deep: #f47a20;
    --orange-light: #fba54a;
    --ink: #3d4450;
    --white: #ffffff;
    --paper: #f3f4f5;
    --facet: #e8eaec;
    --navy: #1f4e79;
    --sky: #a9cfe0;
    --sky-line: #a6d1e3;
    --scene-top: #7fa9c4;
  }
  html, body {
    margin: 0;
    padding: 0;
    width: 1200px;
    height: 457px;
    overflow: hidden;
    background: var(--white);
  }
  .cover {
    position: relative;
    width: 1200px;
    height: 457px;
    overflow: hidden;
    background: var(--paper);
    font-family: "Montserrat", sans-serif;
  }
  .cover__shapes {
    position: absolute;
    inset: 0;
    width: 1200px;
    height: 457px;
  }
  .cover__copy {
    position: absolute;
    left: 0;
    top: 0;
    width: 540px;
    height: 457px;
    text-align: center;
  }
  .cover__kicker {
    position: absolute;
    left: 0;
    width: 520px;
    top: 66px;
    margin: 0;
    font-size: 25px;
    font-weight: 700;
    color: var(--ink);
    letter-spacing: -0.2px;
  }
  .cover__headline {
    position: absolute;
    left: 0;
    width: 545px;
    top: 112px;
    margin: 0;
    font-size: 58px;
    line-height: 62px;
    font-weight: 800;
    color: var(--white);
    letter-spacing: -0.5px;
  }
  .cover__tagline {
    position: absolute;
    left: 0;
    width: 530px;
    top: 324px;
    margin: 0;
    font-size: 19px;
    line-height: 32px;
    font-weight: 700;
    color: var(--ink);
  }
  .brand {
    position: absolute;
    right: 22px;
    top: 30px;
    display: flex;
    align-items: center;
    gap: 10px;
  }
  .brand__name {
    font-size: 32px;
    font-weight: 800;
    color: var(--orange);
    letter-spacing: 0.5px;
  }
  .brand__dot {
    width: 36px;
    height: 36px;
    border-radius: 50%;
    background: var(--orange);
  }
</style>
</head>
<body>
<main class="cover">
  <svg class="cover__shapes" viewBox="0 0 1200 457">
    <defs>
      <radialGradient id="orange-glow" cx="0.45" cy="0.45" r="0.7">
        <stop offset="0" stop-color="var(--orange-light)"/>
        <stop offset="1" stop-color="var(--orange-deep)"/>
      </radialGradient>
      <linearGradient id="scene-tone" x1="0" y1="0" x2="0" y2="1">
        <stop offset="0" stop-color="var(--scene-top)"/>
        <stop offset="1" stop-color="var(--sky)"/>
      </linearGradient>
    </defs>

    <polygon points="700,0 1000,0 880,160" fill="var(--facet)"/>
    <polygon points="1000,0 1200,0 1200,200 1080,120" fill="#eceef0"/>
    <polygon points="960,300 1200,230 1200,457 1040,457" fill="var(--facet)"/>

    <path d="M0,0 L560,0 C520,70 470,140 500,210 C535,290 650,300 640,370 C632,420 590,440 585,457 L0,457 Z"
          fill="none" stroke="var(--sky-line)" stroke-width="14"/>
    <path d="M0,0 L545,0 C505,70 455,140 485,212 C520,292 632,304 623,370 C616,418 576,440 572,457 L0,457 Z"
          fill="url(#orange-glow)"/>

    <path d="M0,0 L70,0 C52,18 30,36 0,52 Z" fill="var(--navy)"/>

    <rect role="img"
          aria-label="Illustration: a head in profile with a blue cloud-like brain, a person on a ladder watering it, gears floating around"
          x="660" y="30" width="400" height="440" rx="60"
          fill="url(#scene-tone)"/>

    <circle cx="1200" cy="405" r="58" fill="var(--orange)"/>
  </svg>

  <section class="cover__copy">
    <p class="cover__kicker">In the middle of a storm</p>
    <h1 class="cover__headline">I’m always<br>with you</h1>
    <p class="cover__tagline">breakthrough approach to<br>mental health that’s grounded<br>in science</p>
  </section>

  <div class="brand">
    <span class="brand__name">PIM</span>
    <span class="brand__dot"></span>
  </div>
</main>
</body>
</html>
```